New Van wrap for fertilization and pest control side

We are an existing landscape construction company, growing our fertilzation and pest control side of the business, and looking to add a standard wrap or vinyl to our new fert vans. We want to see bright colors that grab vision to the vehicles, we have large box trucks for out landscape maintenance crews which do a nice job but really want people to recognize these vans for fertilization and pest control
Target Market(s)
people driven for quality service and safe for their home and kids
Requirements
Must have
- bright colors, must send the message that we are a safe fertilization and pest control company
Nice to have
- could use a cartoon character or animal dressed up to show the service
Should not have
- not to wordy going on large vans, our company name is Ridgefold Landscape but we do own the url RF fert if you think that is something that would make sense

```html
<!DOCTYPE html>
<html lang="en">
<head>
<meta charset="utf-8">
<title>Ridgefold Landscape – Fert Van Wrap</title>
<link rel="stylesheet" href="https://fonts.googleapis.com/css2?family=Rubik:wght@500;700;800&display=swap">
<style>
  :root{
    --bg:#ffffff;
    --body-white:#e9e9e9;
    --green-deep:#0a8a3c;
    --green-lime:#9cc62a;
    --orange:#e0742a;
    --orange-deep:#c4482a;
    --tyre:#1d1d1d;
    --rim:#8a8a8a;
    --glass:#56645f;
    --bumper:#2b2b2b;
    --light-red:#d8232a;
    --shadow:#d4d4d4;
  }
  html,body{margin:0;padding:0;width:1200px;height:1200px;overflow:hidden;background:var(--bg);}
  .wrap-sheet{display:block;width:1200px;height:1200px;}
  .brand{font-family:"Rubik",sans-serif;font-weight:800;}
  .brand-first{fill:var(--orange);}
  .brand-second{fill:var(--green-deep);}
  .tag-lawn{font-family:"Rubik",sans-serif;font-weight:700;fill:var(--orange);font-size:24px;letter-spacing:1px;}
  .tag-pest{font-family:"Rubik",sans-serif;font-weight:700;fill:var(--green-deep);font-size:24px;letter-spacing:4px;}
  .phone{font-family:"Rubik",sans-serif;font-weight:700;fill:#fff;font-size:32px;letter-spacing:4px;}
  .tyre{fill:var(--tyre);}
  .rim{fill:var(--rim);stroke:#5a5a5a;stroke-width:6;}
  .glass{fill:var(--glass);}
  .bumper{fill:var(--bumper);}
  .lamp{fill:var(--light-red);}
</style>
</head>
<body>
<svg class="wrap-sheet" viewBox="0 0 1920 1920" xmlns="http://www.w3.org/2000/svg">
  <defs>
    <linearGradient id="greenSweep" x1="0" y1="0" x2="1" y2="0">
      <stop offset="0" stop-color="#0e8a3a"/>
      <stop offset="0.45" stop-color="#8cc22c"/>
      <stop offset="1" stop-color="#0a8a3c"/>
    </linearGradient>
    <linearGradient id="stripeSweep" x1="0" y1="0" x2="1" y2="0">
      <stop offset="0" stop-color="#0a8a3c"/>
      <stop offset="0.5" stop-color="#b8d42a"/>
      <stop offset="1" stop-color="#2da447"/>
    </linearGradient>
    <linearGradient id="orangeBand" x1="0" y1="0" x2="1" y2="0">
      <stop offset="0" stop-color="#c4482a"/>
      <stop offset="0.5" stop-color="#e89a2a"/>
      <stop offset="1" stop-color="#c4482a"/>
    </linearGradient>
    <linearGradient id="artTone" x1="0" y1="0" x2="1" y2="1">
      <stop offset="0" stop-color="#3a55a8"/>
      <stop offset="1" stop-color="#8a6a2a"/>
    </linearGradient>
    <clipPath id="sideBody">
      <path d="M110 375 H900 Q950 385 975 445 L1115 585 Q1230 630 1265 690 V800 H100 V395 Q100 375 110 375 Z"/>
    </clipPath>
    <g id="sideVan">
      <ellipse cx="690" cy="870" rx="650" ry="30" fill="var(--shadow)"/>
      <g clip-path="url(#sideBody)">
        <rect x="90" y="370" width="1190" height="440" fill="var(--body-white)"/>
        <rect x="100" y="400" width="840" height="12" fill="url(#stripeSweep)"/>
        <rect x="100" y="443" width="880" height="4" fill="#333"/>
        <path d="M90 625 Q200 700 420 680 Q650 650 870 535 L1010 490 L1300 480 V820 H90 Z" fill="url(#orangeBand)"/>
        <path d="M90 655 Q220 710 420 690 Q650 660 880 570 L1060 550 L1300 540 V820 H90 Z" fill="url(#greenSweep)"/>
        <rect x="90" y="745" width="1200" height="70" fill="#1d3a22" opacity="0.55"/>
        <rect x="100" y="790" width="900" height="12" fill="url(#orangeBand)"/>
      </g>
      <path class="glass" d="M862 472 H965 V580 H862 Z"/>
      <path class="glass" d="M975 480 L1100 585 H975 Z"/>
      <rect class="bumper" x="1200" y="725" width="68" height="80" rx="10"/>
      <rect class="bumper" x="98" y="740" width="62" height="65"/>
      <rect class="lamp" x="95" y="630" width="26" height="80" rx="4"/>
      <circle class="tyre" cx="370" cy="800" r="72"/><circle class="rim" cx="370" cy="800" r="48"/>
      <circle class="tyre" cx="1100" cy="800" r="72"/><circle class="rim" cx="1100" cy="800" r="48"/>
    </g>
  </defs>

  <!-- Side view, driver facing right -->
  <g class="van-side van-side--right">
    <use href="#sideVan"/>
    <text class="brand" x="142" y="508" font-size="54"><tspan class="brand-first">Ridgefold</tspan> <tspan class="brand-second">Landscape</tspan></text>
    <text class="tag-lawn" x="205" y="555">Lawn Fertilization</text>
    <text class="tag-pest" x="205" y="593">&amp; Pest Control</text>
    <g role="img" aria-label="Cartoon exterminator in blue uniform chasing a fleeing bug">
      <rect x="455" y="515" width="285" height="215" rx="30" fill="url(#artTone)" opacity="0.55"/>
    </g>
    <text class="phone" x="786" y="692">555-014-2387</text>
  </g>

  <!-- Side view, driver facing left -->
  <g class="van-side van-side--left">
    <use href="#sideVan" transform="translate(1375 690) scale(-1 1)"/>
    <text class="brand" x="540" y="1198" font-size="54"><tspan class="brand-first">Ridgefold</tspan> <tspan class="brand-second">Landscape</tspan></text>
    <text class="tag-lawn" x="970" y="1258">Lawn Fertilization</text>
    <text class="tag-pest" x="970" y="1297">&amp; Pest Control</text>
    <g role="img" aria-label="Cartoon exterminator in blue uniform chasing a fleeing bug">
      <rect x="630" y="1220" width="295" height="210" rx="30" fill="url(#artTone)" opacity="0.55"/>
    </g>
    <text class="phone" x="358" y="1392">555-014-2387</text>
  </g>

  <!-- Front view -->
  <g class="van-front">
    <ellipse cx="1655" cy="875" rx="205" ry="16" fill="var(--shadow)"/>
    <rect class="tyre" x="1480" y="790" width="50" height="75" rx="6"/>
    <rect class="tyre" x="1780" y="790" width="50" height="75" rx="6"/>
    <path d="M1495 375 H1815 Q1830 380 1830 400 L1848 560 V730 H1460 V560 L1480 400 Q1480 380 1495 375 Z" fill="var(--body-white)"/>
    <rect x="1485" y="400" width="340" height="16" fill="url(#stripeSweep)"/>
    <rect x="1466" y="495" width="378" height="40" fill="var(--orange)"/>
    <path d="M1462 585 H1848 V730 H1462 Z" fill="url(#greenSweep)"/>
    <path class="glass" d="M1485 460 H1812 L1825 585 H1475 Z"/>
    <rect class="bumper" x="1422" y="528" width="30" height="50" rx="8"/>
    <rect class="bumper" x="1858" y="528" width="30" height="50" rx="8"/>
    <text class="brand" x="1655" y="632" font-size="27" text-anchor="middle"><tspan class="brand-first">Ridgefold</tspan> <tspan class="brand-second">Landscape</tspan></text>
    <circle cx="1655" cy="657" r="12" fill="none" stroke="#2a5a2a" stroke-width="2"/>
    <rect x="1465" y="650" width="100" height="55" rx="20" fill="#eef0ef"/>
    <rect x="1745" y="650" width="100" height="55" rx="20" fill="#eef0ef"/>
    <rect class="bumper" x="1570" y="678" width="170" height="40"/>
    <rect class="bumper" x="1460" y="725" width="388" height="80" rx="6"/>
    <rect x="1598" y="770" width="110" height="22" fill="#f4f4f4"/>
  </g>

  <!-- Rear view -->
  <g class="van-rear">
    <ellipse cx="1655" cy="1570" rx="205" ry="16" fill="var(--shadow)"/>
    <rect class="tyre" x="1482" y="1480" width="48" height="80" rx="6"/>
    <rect class="tyre" x="1782" y="1480" width="48" height="80" rx="6"/>
    <path d="M1500 1068 H1800 Q1810 1070 1815 1090 L1838 1150 V1450 H1462 V1150 L1485 1090 Q1490 1070 1500 1068 Z" fill="var(--body-white)"/>
    <rect x="1490" y="1090" width="320" height="15" fill="url(#stripeSweep)"/>
    <rect x="1462" y="1305" width="376" height="18" fill="url(#orangeBand)"/>
    <rect x="1462" y="1355" width="376" height="95" fill="url(#greenSweep)"/>
    <line x1="1650" y1="1080" x2="1650" y2="1450" stroke="#bdbdbd" stroke-width="2"/>
    <rect class="lamp" x="1460" y="1323" width="30" height="80" rx="4"/>
    <rect class="lamp" x="1810" y="1323" width="30" height="80" rx="4"/>
    <text class="brand" x="1650" y="1193" font-size="38" text-anchor="middle"><tspan class="brand-first">Ridgefold</tspan></text>
    <text class="brand" x="1650" y="1232" font-size="38" text-anchor="middle"><tspan class="brand-second">Landscape</tspan></text>
    <rect x="1675" y="1408" width="102" height="22" fill="#f4f4f4" stroke="#999" stroke-width="1"/>
    <rect class="bumper" x="1465" y="1450" width="372" height="48"/>
  </g>
</svg>
</body>
</html>
```